Unique Private Wine Label for Wine Bottles (UPDATED BRIEF)

Updated Brief Oct 15, 2017. Please see below!

I am looking for a unique wine label designs for my wine bottles. I create wine and would like to have wine labels for my bottles. I am looking for a main label and then several additional labels with the same design just with the type of wine listed on the label (see below for wine types). This is private wine for family and friends to consume not commercially produced wine.

I would like a rustic, classic or vintage design with some color in the label. I do have a specific name for the wine which i like to call "Fernhollow" . I would like to see different designs.

We would like vintage or classic labels. Please give me a few multiple designs based on above. I also want to have a main label and then incorporate different types of wine into the labels like "Chardonnay" or "Pinot Noir" or "Sauvignon Blanc" or "Caberent Savignon" or "Merlot" below the name of the wine. As an example, the labels will be the same design but the word Sauvignon Blanc will be incorporated into the design for this type of wine label and so on for the other types of wine.

Please let me know if you have any questions.
Updates

Project Deadline Extended
Reason: I Have changed the vision of the design. I would like a classic, rustic or vintage design NOT a beach theme. The brief has been updated as of Oct 15, 2017. Please see updated brief for instructions on new design

Note: I have changed the vision of the design. I would like a classic, rustic or vintage design NOT a beach theme. The brief has been updated as of Oct 15, 2017. Please see updated brief for instructions on new design. I would like new designers to provide new designs! Payment is Guaranteed! Thanks!

Target Market(s)

This is private wine for family and friends to consume not commercially produced wine.

Font styles to use
Decorative
Script

Colors

Designer to choose colors to be used in the design.

Requirements
Must have
• Updated Brief Oct 15, 2017. Please see below!
• I am looking for a unique wine label designs for my wine bottles. I create wine and would like to have wine labels for my bottles. I am looking for a main label and then several additional labels with the same design just with the type of wine listed on the label (see below for wine types). This is private wine for family and friends to consume not commercially produced wine.
• I would like a rustic, classic or vintage design with some color in the label. I do have a specific name for the wine which i like to call "Fernhollow". I would like to see different designs.
• We would like vintage or classic labels. Please give me a few multiple designs based on above. I also want to have a main label and then incorporate different types of wine into the labels like "Chardonnay" or "Pinot Noir" or "Sauvignon Blanc" or "Caberent Savignon" or "Merlot" below the name of the wine. As an example, the labels will be the same design but the word Sauvignon Blanc will be incorporated into the design for this type of wine label and so on for the other types of wine.
• Please let me know if you have any questions.
Nice to have
Should not have
• Please see the updated brief instructions above. I DO NOT WANT A BEACH THEME ANYMORE!

```html
<!DOCTYPE html>
<html lang="en">
<head>
<meta charset="utf-8">
<title>Fernhollow Sauvignon Blanc Label</title>
<link rel="stylesheet" href="https://fonts.googleapis.com/css2?family=Old+Standard+TT:wght@400;700&display=swap">
<style>
  :root {
    --backdrop: #ececec;
    --label-cream: #f3f2ec;
    --frame-grey: #c4c1b8;
    --oval-line: #d9d6ce;
    --ink: #2a2927;
    --wine-red: #8c1c20;
    --ornament-tone: #a8a59e;
  }
  html, body {
    margin: 0;
    padding: 0;
    width: 720px;
    height: 1200px;
    overflow: hidden;
    background: var(--backdrop);
  }
  .canvas {
    position: relative;
    width: 720px;
    height: 1200px;
  }
  .wine-label {
    position: absolute;
    left: 60px;
    top: 30px;
    width: 600px;
    height: 1140px;
  }
  .label-shape { fill: var(--label-cream); }
  .label-frame { fill: none; stroke: var(--frame-grey); stroke-width: 1.5; }
  .brand-name {
    font-family: "Old Standard TT", "Times New Roman", serif;
    font-size: 78px;
    fill: var(--ink);
    letter-spacing: 1px;
  }
  .brand-dot { fill: var(--wine-red); }
  .scene-frame { fill: none; stroke: var(--oval-line); stroke-width: 2; }
  .vineyard-scene { fill: url(#vineyardTones); }
  .flourish { fill: url(#flourishTone); }
  .divider { stroke: #55534f; stroke-width: 1.5; }
  .varietal {
    font-family: "Old Standard TT", "Times New Roman", serif;
    font-size: 35px;
    fill: var(--wine-red);
  }
  .volume {
    font-family: "Old Standard TT", "Times New Roman", serif;
    font-size: 30px;
    font-weight: 700;
    fill: var(--ink);
  }
</style>
</head>
<body>
<div class="canvas">
  <svg class="wine-label" viewBox="0 0 600 1140" xmlns="http://www.w3.org/2000/svg">
    <defs>
      <linearGradient id="vineyardTones" x1="0" y1="0" x2="0" y2="1">
        <stop offset="0" stop-color="#cde9ec"/>
        <stop offset="0.35" stop-color="#b9e0df"/>
        <stop offset="0.5" stop-color="#8cc79a"/>
        <stop offset="0.75" stop-color="#4f9c55"/>
        <stop offset="1" stop-color="#2f7a3a"/>
      </linearGradient>
      <radialGradient id="flourishTone">
        <stop offset="0" stop-color="#8f8c86" stop-opacity="0.55"/>
        <stop offset="1" stop-color="#8f8c86" stop-opacity="0"/>
      </radialGradient>
      <path id="nameArc" d="M 30 420 Q 300 150 570 420"/>
    </defs>

    <path class="label-shape" d="M0 1140 L0 150 C10 150 18 144 18 132 C120 40 200 0 300 0 C400 0 480 40 582 132 C582 144 590 150 600 150 L600 1140 Z"/>
    <path class="label-frame" d="M14 1125 L14 165 C24 165 32 158 32 146 C130 60 210 22 300 22 C390 22 470 60 568 146 C568 158 576 165 586 165 L586 1125 Z"/>
    <line class="label-frame" x1="14" y1="1108" x2="586" y2="1108"/>

    <text class="brand-name"><textPath href="#nameArc" startOffset="50%" text-anchor="middle">FERNHOLLOW</textPath></text>
    <circle class="brand-dot" cx="296" cy="365" r="6"/>

    <ellipse class="scene-frame" cx="296" cy="545" rx="238" ry="172"/>
    <ellipse class="vineyard-scene" cx="296" cy="545" rx="212" ry="140" role="img" aria-label="Hand-drawn vineyard with farmhouse, trees and rows of vines"/>
    <ellipse class="flourish" cx="34" cy="565" rx="32" ry="18" role="img" aria-label="Small scroll flourish"/>
    <ellipse class="flourish" cx="566" cy="565" rx="32" ry="18" role="img" aria-label="Small scroll flourish"/>

    <line class="divider" x1="48" y1="780" x2="548" y2="780"/>
    <ellipse class="flourish" cx="296" cy="806" rx="95" ry="22" role="img" aria-label="Decorative scroll ornament"/>

    <text class="varietal" x="298" y="924" text-anchor="middle">SAUVIGNON BLANC</text>
    <text class="volume" x="298" y="1052" text-anchor="middle">750ML</text>
  </svg>
</div>
</body>
</html>
```